TRUCK WASH OUTDOOR DRIVE THROUGH MENU CONTEST

WE NEED A DRIVE THROUGH MENU WITH OUR SERVICES AND PRICES. I HAVE ATTACHED A FEW EXAMPLES THAT I STARTED.

I WANT THIS TO BE EYE CATCHING WITH BRIGHT COLORS

Target Market(s)

TRUCK WASH AND DETAIL SHOP, TRANSPORTATION.

Requirements
Must have
• INCORPORATE MY LOGO INTO THE SIGN.
• FINAL PROJECT MUST BE IN .AI FORMAT.
• COMPANY COLORS ARE RED AND BLUE

```html
<!DOCTYPE html>
<html lang="en">
<head>
<meta charset="utf-8">
<title>Rig Rinse Depot – Drive Through Menu</title>
<link rel="stylesheet" href="https://fonts.googleapis.com/css2?family=Bangers&family=Open+Sans:wght@700&display=swap">
<style>
  :root {
    --sky: #2aa9e1;
    --bubble: #1ea4dd;
    --paper: #ffffff;
    --brand-red: #e52a30;
    --tint: rgba(255, 255, 255, 0.28);
    --ghost: rgba(42, 169, 225, 0.12);
  }
  html, body {
    margin: 0;
    padding: 0;
    width: 927px;
    height: 1200px;
    overflow: hidden;
    background: var(--sky);
  }
  .sign {
    position: relative;
    width: 927px;
    height: 1200px;
    background: var(--sky);
    overflow: hidden;
  }
  .sign__panel {
    position: absolute;
    inset: 0;
  }
  .corner-name {
    position: absolute;
    left: 50px;
    top: 20px;
    margin: 0;
    font-family: "Bangers", cursive;
    font-weight: 400;
    color: var(--paper);
    font-size: 46px;
    line-height: 0.95;
    letter-spacing: 1px;
  }
  .corner-art {
    position: absolute;
    left: 668px;
    top: 28px;
    width: 180px;
    height: 155px;
    border-radius: 24px;
    background: var(--tint);
  }
  .brand-name {
    position: absolute;
    left: 264px;
    width: 400px;
    top: 92px;
    margin: 0;
    text-align: center;
    font-family: "Bangers", cursive;
    font-weight: 400;
    color: var(--brand-red);
    font-size: 64px;
    line-height: 0.95;
    letter-spacing: 1px;
  }
  .soft-bubble {
    position: absolute;
    left: 103px;
    top: 678px;
    width: 70px;
    height: 70px;
    border-radius: 50%;
    background: var(--ghost);
  }
  .package {
    position: absolute;
    width: 288px;
    height: 288px;
    border-radius: 50%;
    background: var(--bubble);
    color: var(--paper);
    text-align: center;
  }
  .package--platinum { left: 68px;  top: 296px; }
  .package--gold     { left: 571px; top: 296px; }
  .package--silver-a { left: 68px;  top: 818px; }
  .package--silver-b { left: 571px; top: 818px; }
  .package__title {
    position: absolute;
    left: 0;
    right: 0;
    margin: 0;
    font-family: "Bangers", cursive;
    font-weight: 400;
    font-size: 58px;
    line-height: 1;
    letter-spacing: 1px;
  }
  .package__steps {
    position: absolute;
    left: 0;
    right: 0;
    margin: 0;
    font-family: "Open Sans", sans-serif;
    font-weight: 700;
    font-size: 17px;
    line-height: 31px;
  }
  .package--top .package__title { top: 52px; }
  .package--top .package__steps { top: 134px; }
  .package--bottom .package__steps { top: 80px; }
  .package--bottom .package__title { top: 194px; }
  .price {
    position: absolute;
    width: 156px;
    height: 156px;
    border-radius: 50%;
    background: var(--bubble);
    border: 9px solid var(--paper);
    box-sizing: border-box;
    display: flex;
    align-items: center;
    justify-content: center;
    font-family: "Bangers", cursive;
    font-weight: 400;
    font-size: 36px;
    color: var(--paper);
    letter-spacing: 1px;
  }
  .price--platinum { left: 267px; top: 520px; }
  .price--gold     { left: 457px; top: 520px; }
  .price--silver-a { left: 267px; top: 725px; }
  .price--silver-b { left: 457px; top: 725px; }
</style>
</head>
<body>
<main class="sign">
  <svg class="sign__panel" width="927" height="1200" viewBox="0 0 927 1200" aria-hidden="true">
    <rect x="30" y="194" width="867" height="976" rx="68" fill="#ffffff"/>
    <circle cx="464" cy="232" r="206" fill="#ffffff"/>
  </svg>

  <h2 class="corner-name">Rig Rinse<br>Depot</h2>
  <div class="corner-art" role="img" aria-label="White truck front illustration surrounded by soap bubbles"></div>

  <h1 class="brand-name">Rig Rinse<br>Depot</h1>

  <div class="soft-bubble" aria-hidden="true"></div>

  <section class="package package--top package--platinum">
    <h3 class="package__title">Platinum</h3>
    <p class="package__steps">Pre-Soak - Soap and<br>Scrub - Rinse - Tire Shine<br>Platinum Protection</p>
  </section>
  <section class="package package--top package--gold">
    <h3 class="package__title">Gold</h3>
    <p class="package__steps">Pre-Soak - Soap and<br>Scrub - Rinse - Tire Shine<br>Wet X Polish</p>
  </section>
  <section class="package package--bottom package--silver-a">
    <p class="package__steps">Pre-Soak - Soap and<br>Scrub - Rinse - Tire Shine<br>Platinum Protection</p>
    <h3 class="package__title">Silver</h3>
  </section>
  <section class="package package--bottom package--silver-b">
    <p class="package__steps">Pre-Soak - Soap and<br>Scrub - Rinse - Tire Shine<br>Platinum Protection</p>
    <h3 class="package__title">Silver</h3>
  </section>

  <div class="price price--platinum">$ 200.00</div>
  <div class="price price--gold">$ 150.00</div>
  <div class="price price--silver-a">$ 100.00</div>
  <div class="price price--silver-b">$ 50.00</div>
</main>
</body>
</html>
```